New design and build for natural product Nasovera nosespray

We are looking for a new design for an existing website.

Nasovera is a natural product. we have three types of products. Please have a look at the existing site: nasovera-example.com

We are looking for a natural look and feel. This because the products are 100 procent natural.

We would like to have the following site structure (rows) :
- Picture of a person in nature
- Packshot
- Tekst
- 4 blocks for the four nasal issues with pictures
- Tekst
- 3 blocks with pictures to explain experiences from others.
- I think a need an extra white block with tekst (like this example ‘let your dreams come true’

Please have a look at the attached pdf.
page 2 is a idea where the site structure is important.
page 3 is an existing folder. Idear is to keep the folder look and feel in line with the new site design.
page 4-5-6 Element that are posible.
page 7 design that is too much.

Beside the home page I would like to have a template for the sales page.

The existing site has a large woocommerce customer database. This must stay available.
I have a staging site available where you can build the site. From here we can export and import the new disgn to the production site.

Please make the site in Divi

```html
<!DOCTYPE html>
<html lang="nl">
<head>
<meta charset="utf-8">
<title>Nasovera – Weer vrij ademen door de neus</title>
<link href="https://fonts.googleapis.com/css2?family=Josefin+Sans:wght@300;400;600;700&family=Raleway:wght@400;500;600;700&display=swap" rel="stylesheet">
<style>
:root{
  --green:#2bb57a;
  --green-dark:#1f9a66;
  --green-light:#5ec7a4;
  --mint-bg:#eef7f4;
  --ink:#3b3f3c;
  --text:#555b57;
  --grey-bar:#ededed;
  --red:#d9181f;
  --olive-a:#5d6b5a;
  --olive-b:#2f3b2e;
  --white:#ffffff;
}
*{box-sizing:border-box;margin:0;padding:0}
html,body{width:1200px;height:3512px;overflow:hidden}
body{position:relative;font-family:'Raleway',sans-serif;color:var(--text);background:var(--white)}
.abs{position:absolute}
.heading{font-family:'Josefin Sans',sans-serif}

/* top bar */
.topbar{left:0;top:0;width:1200px;height:30px;background:var(--grey-bar);font-size:11px;color:var(--ink);font-weight:600}
.topbar .usp{top:8px;display:flex;align-items:center;gap:6px}
.tick{width:15px;height:15px}
.topbar .account{right:143px;top:9px;font-weight:500;font-size:11px}

/* header */
.header{left:0;top:30px;width:1200px;height:90px;background:var(--white)}
.logo{left:130px;top:20px;display:flex;align-items:center;gap:10px}
.logo-mark{width:26px;height:26px;background:var(--green);border-radius:50%}
.logo-name{font-family:'Josefin Sans',sans-serif;font-weight:700;font-size:30px;color:var(--ink)}
.nav a{position:absolute;top:37px;font-size:16px;color:var(--ink);text-decoration:none;font-family:'Raleway',sans-serif}
.nav a.active{font-weight:700}
.nav .active-line{left:348px;top:86px;width:72px;height:3px;background:var(--green)}
.shop-btn{left:930px;top:30px;width:95px;height:33px;border-radius:17px;background:var(--red);color:#fff;font-weight:700;font-size:15px;display:flex;align-items:center;justify-content:center}
.cart{left:1038px;top:33px}

/* hero */
.hero{left:0;top:120px;width:1200px;height:596px;background:linear-gradient(100deg,#3e6a2a 0%,#6e9a3c 35%,#4d7d33 60%,#233d1b 100%)}
.hero-title{left:136px;top:164px;font-family:'Josefin Sans',sans-serif;font-weight:700;font-size:50px;line-height:54px;color:#fff}
.hero-sub{left:142px;top:278px;font-family:'Josefin Sans',sans-serif;font-weight:600;font-size:18px;line-height:26px;color:#fff;width:380px}
.btn{display:flex;align-items:center;justify-content:center;background:var(--green);color:#fff;font-weight:700;letter-spacing:1px;text-transform:uppercase;border-radius:0 14px 0 14px}
.hero .btn{left:142px;top:357px;width:174px;height:47px;font-size:14px;font-family:'Josefin Sans',sans-serif}
.arrow{top:240px}

/* product */
.packshot{left:95px;top:784px;width:465px;height:450px;background:radial-gradient(ellipse at 45% 50%,#d53a32 0%,#c61f1f 30%,#e9f3ee 60%,#ffffff 80%)}
.product-kicker{left:601px;top:822px;font-family:'Josefin Sans',sans-serif;font-weight:300;font-size:33px;color:var(--green)}
.product-title{left:601px;top:860px;font-family:'Josefin Sans',sans-serif;font-weight:700;font-size:33px;color:var(--ink)}
.product-title span{color:var(--green)}
.underline{height:3px;background:var(--green)}
.product-text{left:603px;top:922px;width:460px;font-size:14.5px;line-height:23px}
.feature{display:flex;align-items:center;gap:10px;font-size:13px;font-weight:600;color:var(--ink);line-height:19px}
.feature svg{width:34px;height:34px;flex:none}

/* conditions */
.conditions{left:0;top:1312px;width:1200px;height:588px;background:linear-gradient(120deg,#5ec7a4 0%,#3dbb8a 55%,#25b073 100%)}
.sec-title{width:1200px;text-align:center;font-family:'Josefin Sans',sans-serif;font-size:35px;font-weight:300}
.sec-title b{font-weight:700}
.conditions .sec-title{top:48px;color:#fff}
.conditions .underline{left:567px;top:97px;width:66px;background:#fff}
.conditions-text{top:116px;left:200px;width:800px;text-align:center;color:#fff;font-size:15.5px;line-height:24px}
.c-card{top:215px;width:220px;height:296px;border:2px solid #fff;text-align:center}
.c-card.light{background:#fff}
.c-photo{width:100%;height:151px}
.c-card h3{margin-top:16px;font-family:'Josefin Sans',sans-serif;font-weight:600;font-size:17px;color:#fff}
.c-card.light h3{color:var(--green)}
.c-card p{margin:6px auto 0;width:190px;font-size:10px;line-height:14px;color:#eafaf2}
.c-card.light p{color:var(--text)}
.c-card .btn{position:absolute;left:55px;bottom:16px;width:110px;height:30px;font-size:9px;background:#4a5048;border-radius:0 10px 0 10px}
.c-card.light .btn{background:var(--green)}

/* banner */
.banner{left:0;top:1900px;width:1200px;height:167px;background:linear-gradient(90deg,var(--olive-a),var(--olive-b))}
.banner-text{left:122px;top:44px;font-family:'Josefin Sans',sans-serif;font-size:31px;line-height:38px;color:#fff;font-weight:300}
.banner-text b{font-weight:700}
.banner .btn{left:864px;top:55px;width:175px;height:49px;font-size:14px;font-family:'Josefin Sans',sans-serif}

/* experiences */
.experiences{left:0;top:2067px;width:1200px;height:610px;background:var(--mint-bg)}
.experiences .sec-title{top:56px;color:var(--ink)}
.experiences .sec-title b{color:var(--green)}
.e-card{top:145px;width:291px;height:386px;background:#fff;box-shadow:0 3px 10px rgba(0,0,0,.08)}
.e-photo{width:100%;height:194px}
.e-card h3{margin:24px 22px 0;font-family:'Josefin Sans',sans-serif;font-weight:600;font-size:17px;line-height:23px;color:var(--ink)}
.e-card p{margin:10px 22px 0;font-size:11.5px;line-height:19px}
.e-card .btn{position:absolute;left:23px;bottom:24px;width:115px;height:31px;font-size:10px}

/* dreams */
.leaf{left:157px;top:2707px;width:211px;height:375px;background:linear-gradient(160deg,#d9f1e6,#bfe6d4)}
.dreams-title{left:454px;top:2760px;font-family:'Josefin Sans',sans-serif;font-size:40px;font-weight:300;color:var(--ink)}
.dreams-title b{color:var(--green);font-weight:700}
.dreams-line{left:454px;top:2811px;width:58px}
.dreams-text{left:454px;top:2840px;width:600px;font-size:14.5px;line-height:23px}
.dreams-text p+p{margin-top:26px}
.dreams .btn{left:450px;top:3012px;width:153px;height:44px;font-size:13px;text-transform:uppercase}

/* footer */
.footer{left:0;top:3146px;width:1200px;height:308px;background:linear-gradient(90deg,#2fb57d,#5cc7a3)}
.f-col{top:45px;border-left:3px solid #fff;padding-left:22px}
.f-col h4{font-family:'Josefin Sans',sans-serif;font-weight:600;font-size:18px;color:#fff;margin-top:2px;margin-bottom:20px}
.f-col li{list-style:none;font-size:11px;line-height:23px;color:#eafff4}
.social{display:flex;gap:12px;margin-top:10px}
.social span{width:20px;height:20px;border:2px solid #fff;border-radius:50%}
.copyright{left:0;top:3454px;width:1200px;height:58px;background:var(--green-dark);color:#fff;font-size:11px;text-align:center;line-height:58px}
</style>
</head>
<body>

<div class="abs topbar">
  <div class="abs usp" style="left:130px"><svg class="tick" viewBox="0 0 16 16"><circle cx="8" cy="8" r="8" fill="#2bb57a"/><path d="M4.5 8.2l2.3 2.3 4.7-4.8" stroke="#fff" stroke-width="1.8" fill="none"/></svg>Verzendkosten 2,95 euro in NL</div>
  <div class="abs usp" style="left:460px"><svg class="tick" viewBox="0 0 16 16"><circle cx="8" cy="8" r="8" fill="#2bb57a"/><path d="M4.5 8.2l2.3 2.3 4.7-4.8" stroke="#fff" stroke-width="1.8" fill="none"/></svg>Op werkdagen besteld de volgend dag verzonden.</div>
  <div class="abs account">Inloggen &nbsp;|&nbsp; Winkelmand</div>
</div>

<header class="abs header">
  <div class="abs logo"><span class="logo-mark"></span><span class="logo-name">Nasovera</span></div>
  <nav class="nav">
    <a class="active" style="left:350px">Product</a>
    <a style="left:462px">Onderzoek</a>
    <a style="left:593px">Ervaringen</a>
    <a style="left:721px">Tips/Info</a>
    <a style="left:836px">Contact</a>
    <div class="abs active-line"></div>
  </nav>
  <div class="abs shop-btn">Shop</div>
  <svg class="abs cart" width="24" height="22" viewBox="0 0 24 22"><path d="M1 2h4l3 12h12l3-9H7" fill="none" stroke="#2bb57a" stroke-width="2.2"/><circle cx="10" cy="19" r="2" fill="#2bb57a"/><circle cx="18" cy="19" r="2" fill="#2bb57a"/></svg>
</header>

<section class="abs hero" role="img" aria-label="Photo of a smiling woman breathing fresh air in a green forest">
  <h1 class="abs hero-title">Weer vrij ademen<br>door de neus</h1>
  <p class="abs hero-sub">Lorem Ipsum is simply dummy text of the printing and typesetting industry.</p>
  <div class="abs btn">Get started</div>
  <svg class="abs arrow" style="left:28px" width="26" height="52" viewBox="0 0 26 52"><path d="M24 2L2 26l22 24" fill="none" stroke="#fff" stroke-width="2.5"/></svg>
  <svg class="abs arrow" style="left:1138px" width="26" height="52" viewBox="0 0 26 52"><path d="M2 2l22 24L2 50" fill="none" stroke="#fff" stroke-width="2.5"/></svg>
</section>

<section class="product">
  <div class="abs packshot" role="img" aria-label="Packshot of the red Nasovera box and nasal spray bottle with a green leaf drawing"></div>
  <div class="abs product-kicker">Originele Formule</div>
  <h2 class="abs product-title"><span>100% natuurlijke</span> neusspray</h2>
  <div class="abs underline" style="left:603px;top:903px;width:58px"></div>
  <p class="abs product-text">Nasovera neusspray is vooral effectief bij chronische neusklachten. De formules helpen om vrijer door de neus te ademen en geven verlichting bij verstopte holtes en druk in het voorhoofd</p>

  <div class="abs feature" style="left:601px;top:1022px"><svg viewBox="0 0 34 34"><path d="M6 30C10 18 18 10 30 5M12 22c-4-2-6-6-6-11M18 16c0-5 2-9 6-11" fill="none" stroke="#2bb57a" stroke-width="1.6"/></svg>100% natural</div>
  <div class="abs feature" style="left:836px;top:1022px"><svg viewBox="0 0 34 34"><rect x="3" y="5" width="28" height="25" rx="2" fill="none" stroke="#2bb57a" stroke-width="1.6"/><path d="M3 11h28M9 2v6M25 2v6M8 16h4M15 16h4M22 16h4M8 22h4M15 22h4" stroke="#2bb57a" stroke-width="1.6"/></svg>Long-term use</div>
  <div class="abs feature" style="left:601px;top:1077px"><svg viewBox="0 0 34 34"><circle cx="17" cy="13" r="10" fill="none" stroke="#2bb57a" stroke-width="1.6"/><circle cx="17" cy="13" r="5" fill="none" stroke="#2bb57a" stroke-width="1.6"/><path d="M11 21l-2 11 8-4 8 4-2-11" fill="none" stroke="#2bb57a" stroke-width="1.6"/></svg>Proven effective</div>
  <div class="abs feature" style="left:836px;top:1077px"><svg viewBox="0 0 34 34"><circle cx="17" cy="9" r="6" fill="none" stroke="#2bb57a" stroke-width="1.6"/><path d="M5 33v-8c0-5 5-8 12-8s12 3 12 8v8" fill="none" stroke="#2bb57a" stroke-width="1.6"/></svg>Recommended by<br>ENT doctors</div>
  <div class="abs feature" style="left:601px;top:1137px"><svg viewBox="0 0 34 34"><path d="M17 3c-3 8-7 14-7 20a7 7 0 0 0 14 0c0-6-4-12-7-20z" fill="none" stroke="#2bb57a" stroke-width="1.6"/></svg>Naturally strengthens<br>your nasal mucosa</div>
  <div class="abs feature" style="left:836px;top:1148px"><svg viewBox="0 0 34 34"><path d="M15 3c0 8-9 16-9 22a5 5 0 0 0 5 5c2 0 3-1 6-1s4 1 6 1a5 5 0 0 0 5-5c0-6-9-14-9-22" fill="none" stroke="#2bb57a" stroke-width="1.6"/></svg>Against runny nose, stuffy<br>nose &amp; chronic colds</div>
</section>

<section class="abs conditions">
  <h2 class="abs sec-title">Chronische <b>Neuklachten</b></h2>
  <div class="abs underline"></div>
  <p class="abs conditions-text">Nasovera neusspray is vooral effectief bij chronische neusklachten. De formules helpen om vrijer door de neus te ademen en geven verlichting bij verstopte holtes en druk in het voorhoofd</p>

  <div class="abs c-card light" style="left:130px">
    <div class="c-photo" role="img" aria-label="Photo of a woman with a blocked nose holding a tissue" style="background:linear-gradient(135deg,#c9ccd0,#9aa3ad)"></div>
    <h3>Verstopte neus</h3>
    <p>Een verstopte neus komt meestal voort uit een opgelopen verkoudheid.</p>
    <div class="btn">Learn more</div>
  </div>
  <div class="abs c-card" style="left:369px">
    <div class="c-photo" role="img" aria-label="Photo of a woman with a runny nose blowing into a tissue" style="background:linear-gradient(135deg,#b09a8a,#5e4a40)"></div>
    <h3>Loopneus</h3>
    <p>Wanneer de neus teveel slijm aanmaakt kan daarbij ook extra vocht vrijkomen.</p>
    <div class="btn">Learn more</div>
  </div>
  <div class="abs c-card" style="left:607px">
    <div class="c-photo" role="img" aria-label="Photo of a man pressing his nose bridge with sinus pain" style="background:linear-gradient(135deg,#8c8f93,#4d5155)"></div>
    <h3>Sinusitis</h3>
    <p>Voorhoofdsholteontsteking wordt vooral veroorzaakt door een verkoudheid.</p>
    <div class="btn">Learn more</div>
  </div>
  <div class="abs c-card" style="left:846px">
    <div class="c-photo" role="img" aria-label="Photo of a man using a nasal spray" style="background:linear-gradient(135deg,#d8d6d2,#9d958c)"></div>
    <h3>Neussprayverslaving</h3>
    <p>De meeste (niet-natuurlijke) neussprays kunnen maar een week worden gebruikt.</p>
    <div class="btn">Learn more</div>
  </div>
</section>

<section class="abs banner">
  <p class="abs banner-text">Wil je meer lezen over<br><b>ervaringen van anderen?</b></p>
  <div class="abs btn">Get started</div>
</section>

<section class="abs experiences">
  <h2 class="abs sec-title">Our <b>Customer Experience</b></h2>
  <article class="abs e-card" style="left:140px">
    <div class="e-photo" role="img" aria-label="Photo of a person with a headache holding their head at a table" style="background:linear-gradient(160deg,#8ea2b0,#6a5a48)"></div>
    <h3>Hoofdpijn door verstopte neus</h3>
    <p>Marieke: &nbsp;Al jarenlang heb ik last van een verstopte neus en aanhoudende hoofdpijn doordat ik</p>
    <div class="btn">Learn more</div>
  </article>
  <article class="abs e-card" style="left:458px">
    <div class="e-photo" role="img" aria-label="Photo of a smiling woman at home" style="background:linear-gradient(160deg,#8a7a6a,#3c2f27)"></div>
    <h3>Niezen, mijn neus reageert overal op. Nasovera hielp.</h3>
    <p>Marieke: &nbsp;Al jarenlang heb ik last van een verstopte neus en aanhoudende</p>
    <div class="btn">Learn more</div>
  </article>
  <article class="abs e-card" style="left:772px">
    <div class="e-photo" role="img" aria-label="Photo of a man on a sofa blowing his nose" style="background:linear-gradient(160deg,#eef0f0,#a9adb0)"></div>
    <h3>Verkouden door airco</h3>
    <p>Marieke: &nbsp;Al jarenlang heb ik last van een verstopte neus en aanhoudende hoofdpijn doordat ik</p>
    <div class="btn">Learn more</div>
  </article>
</section>

<section class="dreams">
  <div class="abs leaf" role="img" aria-label="Green line drawing of a leaf branch"></div>
  <h2 class="abs dreams-title">Let your <b>dreams come true</b></h2>
  <div class="abs underline dreams-line"></div>
  <div class="abs dreams-text">
    <p>Lorem Ipsum is simply dummy text of the printing and typesetting industry. Lorem Ipsum has been the industry's standard dummy text ever since the 1500s, when an unknown printer took a galley of type and scrambled it to make.</p>
    <p>It was popularised in the 1960s with the release of Letraset sheets containing Lorem Ipsum passages, and more recently with desktop publishing software.</p>
  </div>
  <div class="abs btn">Learn more</div>
</section>

<footer class="abs footer">
  <div class="abs f-col" style="left:135px">
    <h4>Informatie</h4>
    <ul><li>Privacy verklaring</li><li>Algemene voorwaarden Nasovera</li><li>Zwangerschap</li><li>Gebruiksaanwijzing Nasovera</li><li>neusspray</li></ul>
  </div>
  <div class="abs f-col" style="left:406px">
    <h4>Klanten Service</h4>
    <ul><li>Contact</li><li>Shop</li><li>Verzenden bestelling</li><li>Winkels</li><li>Veel gestelde vragen</li></ul>
  </div>
  <div class="abs f-col" style="left:648px">
    <h4>Contact Us</h4>
    <ul><li>Lindelaan 12</li><li>3700 AB Zeist</li><li>+31 (0)30 -000 12 34</li><li>info@nasovera-example.nl</li><li>&nbsp;</li><li>KvK: 12345678</li><li>BTW nr: NL000.000.000B.01</li></ul>
  </div>
  <div class="abs f-col" style="left:888px">
    <h4>International</h4>
    <ul><li>Frankrijk: nasovera-example.fr</li><li>Engeland: nasovera-example.co.uk</li><li>Spanje: nasovera-example.es</li></ul>
    <div class="social"><span></span><span></span><span></span></div>
  </div>
</footer>
<div class="abs copyright">Copyright 2021 © Nasovera. All Right Reserved</div>

</body>
</html>
```